Carpet cleaning company focused on high quality needs business cards

We are a growing company that just merged with another company and need to design a new business card. We do both residential as well as commercial cleaning. We do carpet, tile & grout, upholstery, hard floors, and stain & pet odor removal. We treat our customers like family and strive to achieve outstanding results with every job.

```html
<!DOCTYPE html>
<html lang="en">
<head>
<meta charset="utf-8">
<title>Ridgeway Steam Crew Cleaning – Business Card</title>
<link rel="stylesheet" href="https://fonts.googleapis.com/css2?family=Open+Sans:wght@400;600;700;800&display=swap">
<style>
  :root {
    --bg: #d9d9d9;
    --card: #ffffff;
    --ink: #1c1b1b;
    --text: #2b2b2b;
    --brand-red: #ee4139;
    --brand-blue: #0a86c6;
  }
  * { box-sizing: border-box; margin: 0; padding: 0; }
  html, body {
    width: 1200px; height: 588px; overflow: hidden;
    background: var(--bg);
    font-family: "Open Sans", Arial, sans-serif;
  }
  .card {
    position: absolute;
    width: 488px; height: 289px;
    background: var(--card);
    border-radius: 22px;
    overflow: hidden;
  }
  .card--front { left: 87px; top: 141px; }
  .card--back { left: 622px; top: 142px; }

  .brand { position: absolute; display: flex; align-items: center; }
  .brand__square { background: var(--brand-red); flex: none; }
  .brand__name {
    font-weight: 800; color: var(--ink);
    line-height: 1.05; letter-spacing: -0.4px;
    white-space: nowrap;
  }
  .card--front .brand { left: 110px; top: 138px; gap: 30px; }
  .card--front .brand__square { width: 104px; height: 104px; }
  .card--front .brand__name { font-size: 29px; }

  .card--back .brand { left: 80px; top: 143px; gap: 15px; }
  .card--back .brand__square { width: 62px; height: 62px; }
  .card--back .brand__name { font-size: 17.5px; }

  .divider {
    position: absolute; left: 282px; top: 76px;
    width: 2px; height: 139px; background: var(--brand-blue);
  }
  .contact { position: absolute; left: 298px; top: 74px; color: var(--text); }
  .contact__name { font-size: 19px; font-weight: 700; color: var(--brand-blue); line-height: 1.2; }
  .contact__name .surname { color: var(--brand-red); }
  .contact__role { font-size: 13.5px; font-weight: 400; color: var(--ink); margin-top: 1px; }
  .contact__list { list-style: none; margin-top: 8px; font-size: 13px; line-height: 17.5px; }
  .contact__list li { display: flex; align-items: center; gap: 4px; white-space: nowrap; }
  .contact__list svg { width: 11px; height: 11px; fill: var(--brand-blue); flex: none; }
  .contact__address { font-size: 13px; line-height: 17px; margin-top: 11px; }

  .swoosh { position: absolute; left: 0; bottom: 0; width: 488px; height: 50px; }
</style>
</head>
<body>
  <section class="card card--front">
    <div class="brand">
      <span class="brand__square"></span>
      <span class="brand__name">Ridgeway<br>Steam Crew<br>Cleaning</span>
    </div>
  </section>

  <section class="card card--back">
    <div class="brand">
      <span class="brand__square"></span>
      <span class="brand__name">Ridgeway<br>Steam Crew<br>Cleaning</span>
    </div>
    <span class="divider"></span>
    <div class="contact">
      <p class="contact__name">Dana <span class="surname">Whitfield</span></p>
      <p class="contact__role">Executive Director</p>
      <ul class="contact__list">
        <li><svg viewBox="0 0 24 24"><path d="M6.6 10.8a15 15 0 0 0 6.6 6.6l2.2-2.2a1 1 0 0 1 1-.25 11.4 11.4 0 0 0 3.6.57 1 1 0 0 1 1 1V20a1 1 0 0 1-1 1A17 17 0 0 1 3 4a1 1 0 0 1 1-1h3.5a1 1 0 0 1 1 1c0 1.250.2 2.450.57 3.57a1 1 0 0 1-.25 1z"/></svg>555 014 2276</li>
        <li><svg viewBox="0 0 24 24"><path d="M2 5h20v2l-10 6L2 7z M2 9l10 6 10-6v10H2z"/></svg>hello@ridgewaysteam.com</li>
        <li><svg viewBox="0 0 24 24"><path d="M12 2a10 10 0 1 0 0 20 10 10 0 0 0 0-20zm6.9 6h-3a15.6 15.6 0 0 0-1.4-3.6A8 8 0 0 1 18.9 8zM12 4c.8 1.2 1.5 2.5 1.9 4h-3.8c.4-1.5 1.1-2.8 1.9-4zM4.3 14a8 8 0 0 1 0-4h3.4a16 16 0 0 0 0 4zm.8 2h3a15.6 15.6 0 0 0 1.4 3.6A8 8 0 0 1 5.1 16zM8 8H5.1a8 8 0 0 1 4.4-3.6C8.9 5.5 8.4 6.7 8 8zm4 12c-.8-1.2-1.5-2.5-1.9-4h3.8c-.4 1.5-1.1 2.8-1.9 4zm2.3-6H9.7a14.6 14.6 0 0 1 0-4h4.6a14.6 14.6 0 0 1 0 4zm.3 5.6c.6-1.1 1.1-2.3 1.4-3.6h3a8 8 0 0 1-4.4 3.6zM16.3 14a16 16 0 0 0 0-4h3.4a8 8 0 0 1 0 4z"/></svg>www.ridgewaysteam.com</li>
      </ul>
      <p class="contact__address">2270 Harbor Lane<br>Lake Briar Point,</p>
    </div>
    <svg class="swoosh" viewBox="0 0 488 50" preserveAspectRatio="none" aria-hidden="true">
      <path d="M10 50 C120 18 260 2 380 0 L488 0 L488 50 Z" fill="var(--brand-red)"/>
      <path d="M86 50 C170 22 300 6 440 3 L488 3 L488 50 Z" fill="#ffffff"/>
      <path d="M96 50 C180 24 310 9 488 6 L488 50 Z" fill="var(--brand-blue)"/>
    </svg>
  </section>
</body>
</html>
```